デザインは年配の方にも読みやすい落ち着いたものを希望します。
今回のイメージと、前回のチラシデータを添付しています。前回は「A4両面カラー」で2種類(添付資料のA・B)制作しましたが、今回は「A3中折カラー」の4ページ1種類にします。前回チラシのaiデータは当選者決定後にお渡し可能です。

デザインは自由にご提案ください。今回のイメージを伝えるために「構成と内容」という資料を添付していますが、このイメージを整えた案でも、内容をふまえてレイアウトを一新した案でも構いません。

文章と写真は弊社で用意します。今回はコピーやコーナー名、レイアウトを中心としたラフデザイン案を募集します。ページ構成と必要な要素は『記載項目』をご覧ください(あわせて添付資料「構成と内容」をご覧ください)。
■1ページ目:表紙
①タイトル ★タイトルはより印象的なものを提案いただきたいです★
②福岡県の地図に約100の蔵元のロゴをレイアウトした図柄(荷印一覧、添付資料「A_表」と概ね同じ)
③麹の里かすみのの文章(添付資料「B_瓦版」の文章を要約したもの)
④寄稿文(新規)
※文字サイズは添付資料「B_瓦版」の本文サイズ程度を想定しています。ただし、用意する文字量にあわせて調整いただくことがあります。
■2ページ目:しょうゆ製造者一覧(添付資料「A_裏」と概ね同じ)
○蔵元の名前・住所(今回は市区町村まで番地不要)・電話番号をリストで掲載。
■3ページ目:「原料・発酵・熟成・製法・特徴・種類・用法・効果」の説明
レイアウトは自由に提案してください。しょうゆに関する8つのキーワードを説明します。添付資料「構成と内容」では丸を並べたレイアウトですが、これに従う必要はありません。もちろんこのイメージを踏襲したレイアウトでも結構です。
■4ページ目:しょうゆを生かした料理レシピ
○料理レシピ(料理名+写真+特徴説明文+レシピ文)を6種類。添付資料「B_郷土料理」に近いイメージですが、料理は変更になります。
提案時は、A4サイズ4ページ、A3サイズ裏表(2ページ)どちらの形式でも構いません。
当選の方には今回PDFで添付している「A_表・裏、B_郷土料理・瓦版」のaiデータはお渡し可能です。

表紙のインパクトを重視してこの案を選定しました。

短い応募期間でしたが、たくさんのご提案をいただき誠にありがとうございます。
多彩な提案をいただいており、クライアントとしても最後まで選定に迷ったようです。結果として1案選定しますが、ご提案いただいた皆さまに感謝申し上げます。
今後、また機会がありましたらぜひよろしくお願いいたします。

```html
<!DOCTYPE html>
<html lang="ja">
<head>
<meta charset="utf-8">
<title>日本一のしょうゆ県 福岡</title>
<link href="https://fonts.googleapis.com/css2?family=Noto+Serif+JP:wght@400;600;700&family=M+PLUS+Rounded+1c:wght@700;800&family=Yuji+Syuku&display=swap" rel="stylesheet">
<style>
:root{
  --red:#c8102e;
  --red-light:#dc4a60;
  --navy:#1d2d55;
  --ink:#333;
  --muted:#777;
  --paper:#fff;
  --soy:#2a0f0c;
}
*{box-sizing:border-box;margin:0;padding:0}
html,body{width:1200px;height:849px;overflow:hidden;background:var(--paper)}
body{position:relative;font-family:"Noto Serif JP",serif;color:var(--ink)}
.spread{position:absolute;inset:0;width:1200px;height:849px}
.top-band{position:absolute;top:0;left:0;width:1200px;height:30px;background:var(--navy)}
.page-left{position:absolute;left:0;top:0;width:600px;height:849px}
.page-right{position:absolute;left:600px;top:0;width:600px;height:849px}
.page-right::before{content:"";position:absolute;left:0;top:30px;bottom:0;width:1px;background:#ddd}

/* left page */
.recipe-head{position:absolute;left:14px;top:30px;width:209px;height:204px;background:var(--red);color:#fff;text-align:center;font-family:"M PLUS Rounded 1c",sans-serif}
.recipe-head h2{margin-top:26px;font-size:21px;line-height:1.35;font-weight:800}
.recipe-head .art{display:block;margin:10px auto 0;width:130px;height:70px;border-radius:50%;background:linear-gradient(#e8495f,#b30d27)}
.recipe-head .sub{position:absolute;left:0;right:0;bottom:16px;font-size:15px;font-weight:700}
.intro{position:absolute;left:235px;top:30px;width:350px;height:204px;background:var(--red);color:#fff;padding:22px 0 0 20px}
.intro p{width:232px;font-size:11.5px;line-height:1.85}
.intro .art{position:absolute;right:16px;top:40px;width:78px;height:140px;border-radius:8px;background:linear-gradient(#d8354d,#b30d27)}

.card{position:absolute;width:276px;height:162px;border:2px solid var(--red);background:#fff;padding:6px 8px}
.card::before{content:"";position:absolute;left:-2px;top:-2px;width:170px;height:4px;background:var(--red)}
.card h3{font-size:13px;color:var(--red);font-weight:700}
.card .photo{position:absolute;right:6px;top:6px;width:90px;height:86px;background:radial-gradient(circle at 45% 45%,#c0652e,#6f3018 70%,#d9c7a8)}
.card .label{font-size:7px;color:var(--red);margin-top:6px}
.card .body{font-size:7px;line-height:1.6;color:#555}
.card .feature{width:160px}
.c1{left:18px;top:246px}.c2{left:310px;top:246px}
.c3{left:18px;top:417px}.c4{left:310px;top:417px}
.c5{left:18px;top:589px}.c6{left:310px;top:589px}

.footer-left{position:absolute;left:0;top:769px;width:600px;height:80px;background:var(--navy);color:#fff;text-align:center}
.footer-left .org{font-size:16px;font-weight:700;margin-top:10px;letter-spacing:.05em}
.footer-left .addr{font-size:9px;margin-top:2px}
.footer-left .tel{font-size:15px;font-weight:700;margin-top:2px;letter-spacing:.04em}

/* right page */
.sun-map{position:absolute;left:87px;top:62px;width:356px;height:356px;border-radius:50%;background:radial-gradient(circle at 52% 45%,#f3d7dc 0,#eab4bd 38%,var(--red-light) 62%,var(--red) 72%)}
.lead{position:absolute;left:42px;top:54px;height:500px;writing-mode:vertical-rl;font-size:15px;line-height:1.5;color:var(--red);letter-spacing:.08em}
.title-lead{position:absolute;left:512px;top:88px;writing-mode:vertical-rl;font-size:24px;font-weight:400;color:var(--red);letter-spacing:.05em}
.title-main{position:absolute;left:478px;top:328px;writing-mode:vertical-rl;font-family:"Yuji Syuku",serif;font-size:76px;line-height:1;color:var(--red)}
.contrib{position:absolute;left:162px;top:410px;width:280px;height:86px;writing-mode:vertical-rl;font-size:8.5px;line-height:1.6;color:var(--muted);overflow:hidden}
.contrib-label{position:absolute;left:458px;top:410px;writing-mode:vertical-rl;font-size:7px;color:var(--muted)}
.dish{position:absolute;left:180px;top:528px;width:218px;height:86px;border-radius:50%;background:radial-gradient(ellipse at 50% 40%,#3b1511,var(--soy) 55%,#fafafa 58%,#e8e8e8)}
.feature-band{position:absolute;left:0;top:630px;width:600px;height:175px;background:var(--navy)}
.feature-box{position:absolute;left:33px;top:640px;width:550px;height:153px;background:#fff}
.feature-text{position:absolute;left:10px;top:10px;width:430px;height:134px;writing-mode:vertical-rl;font-size:8.5px;line-height:1.55;color:var(--muted);overflow:hidden}
.feature-label{position:absolute;left:466px;top:10px;writing-mode:vertical-rl;font-size:7px;color:var(--muted)}
.feature-title{position:absolute;right:8px;top:10px;writing-mode:vertical-rl;font-weight:700;color:var(--navy);font-size:11.5px;line-height:1.3;white-space:nowrap}
.feature-title .big{font-size:16px;color:var(--red);line-height:1.3}
.feature-box .bottle{position:absolute;right:10px;bottom:8px;width:30px;height:48px;border-radius:10px 10px 4px 4px;background:linear-gradient(#f5f5f5,#e6c9ce)}
.footer-right{position:absolute;left:0;right:0;top:818px;text-align:center;font-size:13px;color:var(--ink);letter-spacing:.08em}
</style>
</head>
<body>
<main class="spread">
  <div class="top-band"></div>

  <section class="page-left">
    <header class="recipe-head">
      <h2>しょうゆの国の<br>幸せレシピ</h2>
      <span class="art" role="img" aria-label="鍋と地図のイラスト"></span>
      <p class="sub">福岡の郷土料理</p>
    </header>
    <div class="intro">
      <p>おばあちゃんの煮物、お母さんの汁物、仲間と一緒に囲んだ鍋、大切な人と味わう家庭料理のそばには、使い慣れた地元の醤油がありました。<br>福岡に根差した食文化を支え、『わが家の味』を守り続ける。これが福岡県産醤油の底ヂカラです。</p>
      <span class="art" role="img" aria-label="箸と醤油差しのイラスト"></span>
    </div>

    <article class="card c1"><h3>料理名</h3><span class="photo" role="img" aria-label="料理の写真"></span><p class="label">特徴</p><p class="body feature">地元の醤油で甘辛く煮含めた、家族で囲む定番のおかずです。</p><p class="label">レシピ</p><p class="body">材料を切り、醤油とみりんで煮立てて弱火で煮含める。器に盛り、薬味を添えて仕上げる。</p></article>
    <article class="card c2"><h3>料理名</h3><span class="photo" role="img" aria-label="料理の写真"></span><p class="label">特徴</p><p class="body feature">地元の醤油で甘辛く煮含めた、家族で囲む定番のおかずです。</p><p class="label">レシピ</p><p class="body">材料を切り、醤油とみりんで煮立てて弱火で煮含める。器に盛り、薬味を添えて仕上げる。</p></article>
    <article class="card c3"><h3>料理名</h3><span class="photo" role="img" aria-label="料理の写真"></span><p class="label">特徴</p><p class="body feature">地元の醤油で甘辛く煮含めた、家族で囲む定番のおかずです。</p><p class="label">レシピ</p><p class="body">材料を切り、醤油とみりんで煮立てて弱火で煮含める。器に盛り、薬味を添えて仕上げる。</p></article>
    <article class="card c4"><h3>料理名</h3><span class="photo" role="img" aria-label="料理の写真"></span><p class="label">特徴</p><p class="body feature">地元の醤油で甘辛く煮含めた、家族で囲む定番のおかずです。</p><p class="label">レシピ</p><p class="body">材料を切り、醤油とみりんで煮立てて弱火で煮含める。器に盛り、薬味を添えて仕上げる。</p></article>
    <article class="card c5"><h3>料理名</h3><span class="photo" role="img" aria-label="料理の写真"></span><p class="label">特徴</p><p class="body feature">地元の醤油で甘辛く煮含めた、家族で囲む定番のおかずです。</p><p class="label">レシピ</p><p class="body">材料を切り、醤油とみりんで煮立てて弱火で煮含める。器に盛り、薬味を添えて仕上げる。</p></article>
    <article class="card c6"><h3>料理名</h3><span class="photo" role="img" aria-label="料理の写真"></span><p class="label">特徴</p><p class="body feature">地元の醤油で甘辛く煮含めた、家族で囲む定番のおかずです。</p><p class="label">レシピ</p><p class="body">材料を切り、醤油とみりんで煮立てて弱火で煮含める。器に盛り、薬味を添えて仕上げる。</p></article>

    <footer class="footer-left">
      <p class="org">霞野醤油醸造組合</p>
      <p class="addr">〒800-0012 霞野市大字緑町12</p>
      <p class="tel">TEL／012-345-6781　FAX／012-345-6782</p>
    </footer>
  </section>

  <section class="page-right">
    <div class="sun-map" role="img" aria-label="赤い円の上に福岡県の地図と蔵元の荷印を並べた図柄"></div>
    <p class="lead">福岡はしょうゆ事業者数日本一。<br>地域に根差したしょうゆが息づく日本一のしょうゆ県です。</p>
    <h1 class="title-lead">日本一のしょうゆ県</h1>
    <p class="title-main">福岡</p>
    <p class="contrib-label">寄稿文</p>
    <p class="contrib">醤油は土地の水と気候、そして造り手の手間によって育まれます。県内各地の蔵には、それぞれの町の食卓に寄り添ってきた味があり、甘口から辛口まで実に多彩です。日々の料理に一滴を加えるだけで、懐かしい家庭の味がよみがえります。</p>
    <div class="dish" role="img" aria-label="小皿に注いだ醤油の写真"></div>
    <div class="feature-band"></div>
    <div class="feature-box">
      <p class="feature-text">県内には多くの醤油蔵が点在し、それぞれが地域の食文化とともに歩んできました。原料の大豆や小麦、塩を吟味し、麹を育て、もろみをじっくりと熟成させる工程は、昔ながらの知恵と技の結晶です。甘みのある濃口、色の淡い薄口、刺身に合う再仕込みなど、用途に応じた味わいが揃い、家庭料理から郷土の料理まで幅広く使われています。蔵ごとに異なる香りとコクを食べ比べるのも楽しみのひとつ。地元の醤油は、まさに食の都を支える宝物です。</p>
      <p class="feature-label">文章</p>
      <h2 class="feature-title"><span class="big">『麹の里<br>かすみの』</span><br>食の都は地産醤油の宝庫</h2>
      <span class="bottle" role="img" aria-label="醤油差しのイラスト"></span>
    </div>
    <p class="footer-right">霞野醤油醸造組合</p>
  </section>
</main>
</body>
</html>
```